Heart Rate Game Display Graphic

We need a unique layout / info-graphic for our heart rate software to display an individuals hear rate, HR%, and other data together within a larger class of up to 40 other users. Graphics should be colorful, dynamic, and intuitive.

Target Market(s)

Group Fitness Classes

Font styles to use
Sans Serif

Colors

Designer to choose colors to be used in the design.

Requirements
Must have
• Individual Box must contain data field or graphic representation of:
• User Name
• Heart Rate %
• Points Earned / % Accuracy
Nice to have
• thinking other shape design that easily integrates with 40+ of the same shape. Looking for depth of design and or some 3d visualizations. Competing companies:
• https://www.pulsevane.org/
• https://www.trovo.com/
• https://www.kestra.com/us-en/club
• https://bravulo.com/
• https://dornaly.fit/personal-trainer/
• https://www.quelvanta.io/Solutions/Heart-Rate-Training
• http://wamble.corvinladesystems.com/
• https://pell-tander.com/explore/pell-tander-indoor-cycling-app/
Should not have
• should NOT be just be plain squares representing each client.

```html
<!DOCTYPE html>
<html lang="en">
<head>
<meta charset="utf-8">
<title>Heart Rate Game Display Graphic</title>
<link rel="stylesheet" href="https://fonts.googleapis.com/css2?family=Orbitron:wght@900&family=Barlow:wght@700;800&family=Barlow+Semi+Condensed:wght@700&display=swap">
<style>
  :root {
    --navy: #141626;
    --paper: #f2eeee;
    --bg-light: #eeeeee;
    --bg-mid: #cfcfcf;
    --orange: #f0a51e;
    --orange-deep: #f68b1f;
    --orange-soft: #f2a820;
    --green-deep: #0a9c4a;
    --green-lime: #a6d13a;
    --red: #e23b2e;
    --photo-a: #d7dce4;
    --photo-b: #b7a89a;
    --label: #fbeed6;
  }
  html, body {
    margin: 0;
    padding: 0;
    width: 1200px;
    height: 822px;
    overflow: hidden;
    background: var(--navy);
  }
  .board {
    display: block;
    width: 1200px;
    height: 822px;
  }
  .title-text {
    font-family: "Orbitron", sans-serif;
    font-weight: 900;
    fill: var(--paper);
  }
  .stat-big {
    font-family: "Barlow", sans-serif;
    font-weight: 800;
    fill: var(--navy);
  }
  .rank {
    font-family: "Barlow", sans-serif;
    font-weight: 800;
    fill: var(--paper);
  }
  .player-name {
    font-family: "Barlow Semi Condensed", sans-serif;
    font-weight: 700;
    fill: #ffffff;
  }
  .stat-label {
    font-family: "Barlow", sans-serif;
    font-weight: 700;
    fill: var(--label);
  }
</style>
</head>
<body>
<svg class="board" viewBox="0 0 2324 1593" xmlns="http://www.w3.org/2000/svg">
  <defs>
    <linearGradient id="backdrop-fill" x1="0" y1="0" x2="1" y2="1">
      <stop offset="0" stop-color="var(--bg-light)"/>
      <stop offset="0.5" stop-color="var(--bg-mid)"/>
      <stop offset="1" stop-color="var(--bg-light)"/>
    </linearGradient>
    <linearGradient id="frame-green" x1="0" y1="1" x2="1" y2="0">
      <stop offset="0" stop-color="var(--green-deep)"/>
      <stop offset="1" stop-color="var(--green-lime)"/>
    </linearGradient>
    <linearGradient id="portrait-fill" x1="0" y1="0" x2="1" y2="1">
      <stop offset="0" stop-color="var(--photo-b)"/>
      <stop offset="1" stop-color="var(--photo-a)"/>
    </linearGradient>
  </defs>

  <rect class="frame" x="0" y="0" width="2324" height="1593" fill="var(--navy)"/>
  <rect class="backdrop" x="20" y="20" width="2285" height="1512" fill="url(#backdrop-fill)" role="img" aria-label="Honeycomb pattern of grey hexagons"/>

  <!-- title band -->
  <rect x="118" y="101" width="80" height="111" fill="var(--orange)"/>
  <rect x="2112" y="101" width="80" height="111" fill="var(--orange)"/>
  <rect x="198" y="101" width="1914" height="111" fill="var(--navy)"/>
  <text class="title-text" x="280" y="187" font-size="64" textLength="1740" lengthAdjust="spacingAndGlyphs">HEART RATE GAME DISPLAY GRAPHIC</text>

  <!-- player tile -->
  <g class="player-tile">
    <polygon class="tile-shell" points="945,375 1420,375 1655,785 1420,1195 945,1195 708,785" fill="var(--navy)"/>
    <polygon class="tile-border" points="1003,483 1352,483 1478,703 1555,703 1608,785 1555,867 1470,867 1352,1087 1003,1087 830,785" fill="url(#frame-green)"/>

    <polygon class="portrait" points="1015,508 1085,508 1085,726 1118,785 990,1010 858,785" fill="url(#portrait-fill)" role="img" aria-label="Player portrait photo"/>
    <polygon class="score-panel" points="1085,508 1338,508 1465,726 1085,726" fill="var(--paper)"/>
    <polygon class="name-band" points="1085,726 1555,726 1580,785 1555,845 1085,845 1118,785" fill="var(--navy)"/>
    <polygon class="points-panel" points="1085,845 1290,845 1165,1062 1012,1062 990,1010" fill="var(--orange-deep)"/>
    <polygon class="accuracy-panel" points="1290,845 1465,845 1342,1062 1165,1062" fill="var(--orange-soft)"/>

    <circle class="status-dot" cx="1085" cy="563" r="30" fill="var(--red)"/>

    <text class="stat-big" x="1100" y="682" font-size="104" textLength="285" lengthAdjust="spacingAndGlyphs">100%</text>
    <text class="rank" x="1478" y="683" font-size="62" textLength="62" lengthAdjust="spacingAndGlyphs">#1</text>
    <text class="player-name" x="1155" y="802" font-size="48" textLength="378" lengthAdjust="spacingAndGlyphs">MARLOW DENTRY</text>

    <text class="stat-big" x="1092" y="924" font-size="58" textLength="128" lengthAdjust="spacingAndGlyphs">1200</text>
    <text class="stat-big" x="1280" y="924" font-size="58" textLength="122" lengthAdjust="spacingAndGlyphs">60%</text>

    <text class="stat-label" x="1043" y="999" font-size="32" textLength="114" lengthAdjust="spacingAndGlyphs">POINTS</text>
    <text class="stat-label" x="1030" y="1026" font-size="21" textLength="130" lengthAdjust="spacing">EARNED</text>
    <text class="stat-label" x="1288" y="997" font-size="80" text-anchor="middle" fill="#ffffff">%</text>
    <text class="stat-label" x="1210" y="1026" font-size="21" textLength="142" lengthAdjust="spacing">ACCURACY</text>
  </g>

  <!-- footer -->
  <text class="title-text" x="52" y="1576" font-size="27" textLength="830" lengthAdjust="spacingAndGlyphs">HEART RATE GAME DISPLAY GRAPHIC</text>
  <text class="title-text" x="2188" y="1576" font-size="27" textLength="110" lengthAdjust="spacingAndGlyphs">2020</text>
</svg>
</body>
</html>
```